Velmor Integrated Company Profile

We are looking for a new design for our company profile. We need two output formats. A PDF version to use as a soft copy. Another version is needed for printing.

We are seeking an A4 profile based on the same text content of our old one. Some new content will be provided once the graphics are confirmed.

Attached is our old profile. Please give us a newer design. Once design is confirmed we will provide the new content to use.
I am available for any answers or feedback.

Target Market(s)

This is used for introducing our company to the customers.
We are also seeking investors, so they might be considered

Industry/Entity Type

Information Technology

Requirements
Must have
• Info-graphics based on the data in old profile
• Some info-graphics about number of orders, customers and sales volume
• We have two websites for selling online; nilecallstock.com and dunelinkdepot.com. We need to include them in a way or another in the profile. Their logos are in the attached files.
Nice to have
• Any new suggestions about content to include in the profile will be welcomed

```html
<!DOCTYPE html>
<html lang="en">
<head>
<meta charset="utf-8">
<title>Velmor Integrated – Company Profile</title>
<link href="https://fonts.googleapis.com/css2?family=Oswald:wght@300;400;600&family=Questrial&family=Roboto+Condensed:wght@400;700&display=swap" rel="stylesheet">
<style>
  :root{
    --bg:#e9e9e9;
    --paper:#ffffff;
    --navy:#1b3a6b;
    --orange:#f7931e;
    --salmon:#f5844c;
    --ink:#23406f;
  }
  *{box-sizing:border-box;margin:0;padding:0}
  html,body{width:1200px;height:800px;overflow:hidden;background:var(--bg)}
  .page{position:absolute;background:var(--paper);overflow:hidden}
  .page--profile{left:99px;top:50px;width:471px;height:665px}
  .page--strategy{left:617px;top:88px;width:471px;height:666px}

  .brand{position:absolute;left:378px;top:18px;display:flex;align-items:center;gap:5px;
    font-family:"Oswald",sans-serif;font-weight:600;font-size:17px;color:var(--orange);letter-spacing:1px}
  .brand__mark{width:10px;height:10px;background:var(--navy)}
  .rule{position:absolute;left:0;top:43px;width:367px;height:5px;
    background:linear-gradient(90deg,var(--navy) 0%,var(--navy) 55%,rgba(27,58,107,0) 100%)}

  .tag{position:absolute;left:22px;height:16px;padding-left:14px;color:#fff;background:var(--orange);
    font-family:"Oswald",sans-serif;font-weight:300;font-size:13.5px;line-height:16px;letter-spacing:.4px;
    clip-path:polygon(0 0,100% 0,calc(100% - 12px) 100%,0 100%)}

  .copy{position:absolute;left:22px;width:427px;font-family:"Questrial",sans-serif;font-size:9.6px;
    line-height:14.2px;color:var(--ink);text-align:justify;letter-spacing:.15px}

  .skyline{position:absolute;left:0;bottom:0;width:471px;height:118px;
    background:linear-gradient(180deg,rgba(255,255,255,1) 0%,#9db6df 30%,#2d56a6 58%,#0d1e46 100%)}

  .icon{position:absolute;width:58px;height:58px}
  .step{position:absolute;top:181px;width:141px;height:131px}
  .step__head{height:45px;background:var(--salmon);border-radius:12px 12px 0 0;display:flex;align-items:flex-end;
    justify-content:center;padding-bottom:5px;font-family:"Oswald",sans-serif;font-weight:600;font-size:15px;
    color:#fff;letter-spacing:.8px}
  .step__body{height:86px;border:2px solid var(--salmon);border-top:none;border-radius:0 0 12px 12px;padding:8px 6px 0 18px}
  .step__body li{font-family:"Roboto Condensed",sans-serif;font-size:8px;line-height:14.3px;color:var(--navy);
    text-transform:uppercase;list-style:none;position:relative}
  .step__body li::before{content:"";position:absolute;left:-5px;top:6px;width:2px;height:2px;background:var(--salmon)}
  .step__num{position:absolute;left:50%;top:-12px;transform:translateX(-50%);width:25px;height:25px;border-radius:50%;
    background:var(--navy);border:2px solid #fff;color:#fff;font-family:"Oswald",sans-serif;font-weight:600;font-size:13px;
    line-height:21px;text-align:center}

  .value{position:absolute;left:24px;width:423px;height:84px;border:2px solid var(--navy);border-radius:12px}
  .value__icon{position:absolute;left:24px;top:6px;width:64px;height:48px}
  .value__name{position:absolute;left:0;width:140px;bottom:6px;text-align:center;font-family:"Oswald",sans-serif;
    font-weight:600;font-size:15px;color:var(--navy);letter-spacing:.8px}
  .value__text{position:absolute;left:129px;right:22px;top:50%;transform:translateY(-50%);
    font-family:"Roboto Condensed",sans-serif;font-size:9.6px;line-height:13.5px;color:var(--navy)}
</style>
</head>
<body>

<section class="page page--profile">
  <div class="brand"><span class="brand__mark"></span>VELMOR</div>
  <div class="rule"></div>

  <h2 class="tag" style="top:61px;width:126px">OVERVIEW</h2>
  <p class="copy" style="top:86px">Velmor Integrated Solutions founded in 2003 in Egypt, Velmor expanded into a new Branch in Saudi Arabia. And currently its customers are located in more than 20 countries around the globe. Velmor made the requisite investment in technical expertise and Go-to-market capabilities to address the complex unified communication needs of its Customers, gaining the UC market leadership day after day.</p>

  <h2 class="tag" style="top:162px;width:126px">OUR VISION</h2>
  <p class="copy" style="top:185px">To be the unified communication trusted partner of Businesses, Governments and NGOs around the globe.</p>

  <h2 class="tag" style="top:218px;width:126px">OUR MISSION</h2>
  <p class="copy" style="top:242px">To continuously work on integrating real-time enterprise communication services that includes but not limited to instant messaging, VOIP , Call Center ,mobility features video conferencing, data sharing and call control with non-real-time communication services such as unified messaging (integrated voicemail, e-mail, SMS and fax). UC is not necessarily a single product, but a set of products that provides a consistent unified user-interface and user-experience across multiple devices and media types.</p>

  <h2 class="tag" style="top:332px;width:126px">OUR CULTURE</h2>
  <p class="copy" style="top:355px">At Velmor, we Provide our customers the best solution that fits their business. We eliminate behavioral barriers to UC adoption and help companies create an irresistible culture of collaboration from a distance.<br>Hiring and retaining the best professionals is the key to our success. That is why we only hire the best of the best personnel. All of our professionals undergo extensive training on our philosophy and methodology of providing world-class service and solutions to our customers.<br>Our company environment is professional, challenging, rewarding, creative and respectful of ideas and individuals- all key factors to successfully deliver services and solutions to our customers. Our team of industry-expert staff provides you with world-class expertise and service, our staff become a virtual extension of our client's staff. At Velmor, we are committed to be an extension of your department. We take a highly flexible approach that enables us to meet our client's needs within the business Management concepts. We work hard to continuously deliver Value and are fully accountable as a single, local point of contact.</p>

  <div class="skyline" role="img" aria-label="Photo of a lit bridge over water with a city skyline at night"></div>
</section>

<section class="page page--strategy">
  <div class="brand"><span class="brand__mark"></span>VELMOR</div>
  <div class="rule"></div>

  <h2 class="tag" style="top:67px;width:132px">OUR STRATEGY</h2>

  <svg class="icon" style="left:58px;top:96px" viewBox="0 0 58 58" fill="none" stroke="#f5844c" stroke-width="3">
    <rect x="4" y="14" width="44" height="30" rx="2"/>
    <path d="M20 44v6M32 44v6M14 52h24" stroke-linecap="round"/>
    <path d="M22 34l28-30" stroke-width="3.5" stroke-linecap="round"/>
    <path d="M16 38c2-6 6-6 8-4s0 6-8 4z" fill="#f5844c"/>
  </svg>

  <svg class="icon" style="left:207px;top:98px" viewBox="0 0 58 58" fill="#f5844c">
    <path d="M18 14l4 0 1 5 4 2 4-3 3 3-3 4 2 4 5 1v4l-5 1-2 4 3 4-3 3-4-3-4 2-1 5h-4l-1-5-4-2-4 3-3-3 3-4-2-4-5-1v-4l5-1 2-4-3-4 3-3 4 3 4-2z"/>
    <circle cx="20" cy="32" r="5" fill="#fff"/>
    <path d="M42 4h3l1 3 3 1 2-2 2 2-2 2 1 3 3 1v3l-3 1-1 3 2 2-2 2-2-2-3 1-1 3h-3l-1-3-3-1-2 2-2-2 2-2-1-3-3-1v-3l3-1 1-3-2-2 2-2 2 2 3-1z"/>
    <circle cx="43.5" cy="14" r="3" fill="#fff"/>
    <path d="M42 34h3l1 3 3 1 2-2 2 2-2 2 1 3 3 1v3l-3 1-1 3 2 2-2 2-2-2-3 1-1 3h-3l-1-3-3-1-2 2-2-2 2-2-1-3-3-1v-3l3-1 1-3-2-2 2-2 2 2 3-1z"/>
    <circle cx="43.5" cy="44" r="3" fill="#fff"/>
  </svg>

  <svg class="icon" style="left:346px;top:96px" viewBox="0 0 58 58" fill="none" stroke="#f5844c" stroke-width="3">
    <rect x="6" y="8" width="36" height="46" rx="3"/>
    <rect x="16" y="4" width="16" height="8" rx="2" fill="#f5844c"/>
    <path d="M13 22h22M13 30h22M13 38h14M13 46h10" stroke-linecap="round"/>
    <circle cx="44" cy="46" r="10" fill="#f5844c" stroke="#fff" stroke-width="2"/>
    <path d="M39 46l4 4 6-7" stroke="#fff" stroke-width="2.5"/>
  </svg>

  <div class="step" style="left:24px">
    <span class="step__num">1</span>
    <div class="step__head">ASSESS &amp; DESIGN</div>
    <ul class="step__body">
      <li>Business &amp; Technical assessment.</li>
      <li>Client's objective.</li>
      <li>Solution design &amp; TCO analysis.</li>
    </ul>
  </div>
  <div class="step" style="left:166px">
    <span class="step__num">2</span>
    <div class="step__head">IMPLEMENT</div>
    <ul class="step__body">
      <li>Project plan &amp; management.</li>
      <li>Certified technical team.</li>
      <li>Quality assurance.</li>
      <li>Documentation &amp; training.</li>
    </ul>
  </div>
  <div class="step" style="left:307px">
    <span class="step__num">3</span>
    <div class="step__head">FOLLOW UP</div>
    <ul class="step__body">
      <li>ROI and adoption assurance.</li>
      <li>Budget flexible service plans.</li>
      <li>Upgrades and fixes communication.</li>
    </ul>
  </div>

  <h2 class="tag" style="top:346px;width:132px">OUR VALUES</h2>

  <div class="value" style="top:376px">
    <svg class="value__icon" viewBox="0 0 64 48" fill="none" stroke="#f5844c" stroke-width="3" stroke-linejoin="round">
      <path d="M4 14l10-8 6 8-10 8z" fill="#f5844c"/>
      <path d="M60 14l-10-8-6 8 10 8z" fill="#f5844c"/>
      <path d="M14 20l14 16c3 3 6 1 5-2M20 28l10 10c3 2 5 0 4-2M24 22l12 10M46 14c-6-2-12-2-18 4l4 4 8-4 10 10"/>
    </svg>
    <div class="value__name">COMMITMEN</div>
    <p class="value__text">For those who are committed, a promise is a responsibility, and this is how we guarantee a superior service.</p>
  </div>

  <div class="value" style="top:461px">
    <svg class="value__icon" viewBox="0 0 64 48" fill="none" stroke="#f5844c" stroke-width="3" stroke-linejoin="round">
      <rect x="16" y="18" width="7" height="18" fill="#f5844c"/>
      <path d="M26 18l6-10c2-4 6-2 5 2l-2 7h10c3 0 4 3 2 5 2 1 2 4 0 5 2 1 1 4-1 5 1 2-1 4-3 4H26z"/>
      <path d="M22 40l8 6 20-14" stroke-linecap="round"/>
    </svg>
    <div class="value__name">EXPEDIENCY</div>
    <p class="value__text">Accurately and professionally providing the most suitable solution for your needs and perfectly apply it.</p>
  </div>

  <div class="value" style="top:545px">
    <svg class="value__icon" viewBox="0 0 64 48" fill="none" stroke="#f5844c" stroke-width="2.5" stroke-linecap="round">
      <path d="M10 34h10l8 4h12c4 0 4-4 0-4h-8M40 34l12-6c4-2 6 2 3 4l-15 10H20l-10-4z" fill="#f5844c"/>
      <path d="M26 30V18l-4-4M32 30V8M38 30V18l4-4M44 30v-8"/>
      <circle cx="22" cy="12" r="2.5"/><circle cx="32" cy="5" r="2.5"/><circle cx="42" cy="12" r="2.5"/><circle cx="44" cy="19" r="2.5"/>
    </svg>
    <div class="value__name">INGENUITY</div>
    <p class="value__text">Innovating creative techniques for our services and products.</p>
  </div>
</section>

</body>
</html>
```